Website re-design for a Gardening - Vegetable Growing -Compost Ecommerce site

We need a "green & organic" looking web design for The Loamfield Store website re-design. The website sells garden and landscape supplies, and specialises in composites and vegetable growing products which are sold nationwide throughout the UK.

This project is for a homepage & content page design which can be used as a template to create other pages through the site, ideally with css and coding for a joomla template.

Our customer base is made up of gardeners & vegetable growers. The site is an ecommerce site run on Joomla CMS, we will be converting the design into a joomla template.

The Home page will contain information and attractive garden & vegetable growing images linking to information and product / shop category pages.

Current site: www.theloamfieldstore.co.uk

Sites I like the look of :

http://fernpatchplanter.com/index.php
http://keepsake.brovelmedia.com
http://www.tumblerootfolk.co.uk/
http://www.hamletcreamery.co.uk
Updates

Hi Guys! Feel free to use different colour schemes from the three colours i have suggested in the brief. I am open to any suggestions, but a modern look and feel is preferred.

Target Market(s)

Home owners, vegetable growers and keen gardeners

Industry/Entity Type

Landscape

Coding

Coded - Design and coding required

Font styles to use
Sans Serif

Colors
9bcb3c
faa54b
fece3e

Requirements
Must have
• a white main content background

```html
<!DOCTYPE html>
<html lang="en">
<head>
<meta charset="utf-8">
<title>The Loamfield Store – Garden Supplies</title>
<link rel="stylesheet" href="https://fonts.googleapis.com/css2?family=Lato:wght@400;700&display=swap">
<style>
:root{
  --green:#9bcb3c;
  --green-dark:#5f8a26;
  --green-line:#8dbf3a;
  --orange:#faa54b;
  --yellow:#fec100;
  --ink:#222;
  --grey-bg:#f2f2f2;
  --bar:#333;
  --white:#fff;
}
*{margin:0;padding:0;box-sizing:border-box}
html,body{width:1101px;height:1200px;overflow:hidden}
body{position:relative;background:var(--white);font-family:'Lato',sans-serif;color:var(--ink)}
.abs{position:absolute}
.top-strip{left:0;top:0;width:1101px;height:80px;background:var(--grey-bg)}
.header{left:184px;top:0;width:734px;height:124px;background:var(--white);z-index:3}
.brand{left:14px;top:14px;display:flex;align-items:center;gap:8px}
.brand-mark{width:34px;height:34px;border-radius:50%;background:var(--yellow)}
.brand-name{font-size:24px;font-weight:700;color:var(--green);line-height:1;white-space:nowrap}
.contact-top{right:18px;top:12px;font-size:12.5px;display:flex;gap:12px;align-items:center;white-space:nowrap}
.contact-top span{display:flex;align-items:center;gap:6px}
.search{left:419px;top:41px;width:193px;height:27px;border:1px solid #ccc;border-radius:14px;font-size:11px;color:#888;padding:6px 11px}
.search svg{position:absolute;right:10px;top:6px}
.social{display:flex;gap:5px}
.social i{width:18px;height:18px;border-radius:50%;display:block}
.header .social{left:623px;top:44px}
.nav{left:0;top:80px;width:734px;height:44px;border-top:1px solid #e5e5e5;display:flex;align-items:center;font-size:11px;font-weight:700;padding-left:16px;white-space:nowrap}
.nav a{margin-right:21px;color:var(--ink);text-decoration:none}
.nav a.active{color:var(--green);border-bottom:3px solid var(--green);padding:14px 0 13px;margin-top:3px}
.cart{position:absolute;right:20px;top:7px;display:flex;align-items:center;gap:7px;font-size:11px}
.cart-icon{width:27px;height:27px;background:var(--green);border-radius:2px}
.cart b{color:var(--green)}
.hero{left:0;top:80px;width:1101px;height:376px;background:linear-gradient(100deg,#6b7a4e 0%,#4a3a2a 30%,#6f8f3a 55%,#9aa37a 75%,#5a4a38 100%)}
.hero-caption{left:641px;top:272px;width:276px;height:122px;background:rgba(30,30,30,.75);color:var(--white);padding:8px 12px;z-index:2}
.hero-caption h2{font-size:26px;font-weight:700;line-height:32px;white-space:nowrap}
.btn-read{margin-top:10px;display:inline-flex;align-items:center;gap:10px;background:var(--orange);color:var(--white);font-weight:700;font-size:14px;padding:8px 12px;border-radius:2px;white-space:nowrap}
.btn-read i{width:16px;height:16px;border-radius:50%;background:var(--white);display:block}
.dots{left:524px;top:412px;display:flex;gap:5px;z-index:2}
.dots i{width:10px;height:10px;border-radius:50%;background:var(--white);display:block}
.dots i.on{background:var(--orange)}
.footer-band{left:0;top:912px;width:1101px;height:288px;background:var(--green-dark);border-top:4px solid var(--green-line)}
.main{left:182px;top:438px;width:734px;height:548px;background:var(--white);border-top:4px solid var(--green-line);box-shadow:0 1px 2px rgba(0,0,0,.2);z-index:2}
.side-menu{left:5px;top:5px;width:168px;height:195px;background:var(--green)}
.side-menu li{list-style:none;height:28px;line-height:28px;padding-left:14px;font-size:11px;font-weight:700;color:#2d3a10;border-bottom:1px solid #b9dc78}
.promo{left:5px;top:207px;width:168px;height:193px;background:var(--yellow);padding:5px 8px;font-size:11px;color:#3a2d00}
.promo ul{margin-top:6px}
.promo li{list-style:none;display:flex;align-items:center;gap:10px;height:27.5px}
.pay-badge{left:5px;top:407px;width:168px;height:42px;border:1px solid #ccc;background:linear-gradient(#fff,#eee)}
.pay-badge i{position:absolute;left:10px;top:6px;width:28px;height:28px;border-radius:50%;background:#9a9a9a}
.discounts{left:5px;top:455px;width:168px;height:31px;background:var(--green);color:var(--white);font-size:14px;display:flex;align-items:center;gap:10px;padding-left:10px;border-radius:2px}
.section-title{left:180px;top:6px;width:546px;height:29px;background:var(--bar);color:var(--white);font-size:17px;line-height:29px;padding-left:8px;border-bottom:2px solid #555}
.product{width:170px;text-align:center;font-size:14px}
.product .photo{height:118px;display:block}
.product p{margin-top:8px;white-space:nowrap}
.footer-col{top:1010px;color:var(--white);font-size:10px}
.footer-col h3{font-size:13px;font-weight:700;margin-bottom:13px}
.footer-col li{list-style:none;display:flex;align-items:center;gap:6px;height:20.5px}
.footer-col li::before{content:"";width:7px;height:7px;border-radius:50%;border:1px solid #cfe3a9}
.vsep{top:1008px;width:1px;height:138px;background:#7aa13e}
.foot-brand{left:760px;top:1018px;width:150px;text-align:center;color:#cfe0b4;font-size:22px;font-weight:700;line-height:28px}
.foot-brand i{display:block;margin:0 auto 10px;width:34px;height:34px;border-radius:50%;background:#8fb256}
.foot-rule{left:184px;top:1160px;width:732px;height:1px;background:#7aa13e}
.copy{left:184px;top:1174px;color:var(--white);font-size:10px}
.foot-social{left:829px;top:1171px}
</style>
</head>
<body>
<div class="abs top-strip"></div>

<header class="abs header">
  <div class="abs brand"><span class="brand-mark"></span><span class="brand-name">The Loamfield Store</span></div>
  <div class="abs contact-top">
    <span><svg width="14" height="14" viewBox="0 0 14 14"><circle cx="7" cy="7" r="6.5" fill="none" stroke="#9bcb3c"/><path d="M4.5 4c1 3 2.5 4.5 5 5.5l.8-1.3-1.5-.8-.7.7c-1-.5-1.7-1.2-2.2-2.2l.7-.7-.8-1.5z" fill="#9bcb3c"/></svg>0870 555 2146</span>
    <span><svg width="14" height="11" viewBox="0 0 14 11"><rect x=".5" y=".5" width="13" height="10" fill="none" stroke="#faa54b"/><path d="M.5.5 7 6l6.5-5.5" fill="none" stroke="#faa54b"/></svg>info@theloamfieldstore.co.uk</span>
  </div>
  <div class="abs search">Search<svg width="13" height="13" viewBox="0 0 13 13"><circle cx="5.5" cy="5.5" r="4.5" fill="none" stroke="#888" stroke-width="1.5"/><path d="M9 9l3.5 3.5" stroke="#888" stroke-width="1.5"/></svg></div>
  <div class="abs social"><i style="background:#3b5998"></i><i style="background:#4aa3df"></i><i style="background:#1a79b5"></i><i style="background:#d9382c"></i></div>
  <nav class="abs nav">
    <a href="#">HOME</a>
    <a href="#" class="active">PRODUCTS &nbsp;&nbsp;⌄</a>
    <a href="#">ABOUT US ⌄</a>
    <a href="#">GARDEN GURU ⌄</a>
    <a href="#">BULK LOADS</a>
    <a href="#">GO TO</a>
    <div class="cart"><span class="cart-icon"></span><b>CART</b>&nbsp;0 ITEM(S) - $0.00</div>
  </nav>
</header>

<div class="abs hero" role="img" aria-label="Gloved hands planting a vegetable seedling in dark garden soil beside a trowel"></div>
<div class="abs hero-caption">
  <h2>Specialist Vegetable<br>COMPOST &amp; TOPSOIL</h2>
  <span class="btn-read">READ MORE <i></i></span>
</div>
<div class="abs dots"><i></i><i></i><i class="on"></i><i></i></div>

<div class="abs footer-band"></div>

<main class="abs main">
  <ul class="abs side-menu">
    <li>Compost &amp; Manure</li><li>Premium Topsoils</li><li>Grow Your Own</li><li>Lawn Turf</li><li>Raised Bed Kits</li><li>Veg Plug Plants</li>
  </ul>
  <div class="abs promo">
    Order online before 1.00pm for next day delivery or book a delivery date!
    <ul>
      <li><svg width="16" height="16" viewBox="0 0 16 16"><circle cx="8" cy="8" r="7" fill="none" stroke="#3a2d00" stroke-width="1.3"/><path d="M4.8 8.2 7 10.3l4.3-4.5" fill="none" stroke="#3a2d00" stroke-width="1.5"/></svg>Great Value</li>
      <li><svg width="16" height="16" viewBox="0 0 16 16"><circle cx="8" cy="8" r="7" fill="none" stroke="#3a2d00" stroke-width="1.3"/><path d="M4.8 8.2 7 10.3l4.3-4.5" fill="none" stroke="#3a2d00" stroke-width="1.5"/></svg>Quality Service</li>
      <li><svg width="16" height="16" viewBox="0 0 16 16"><circle cx="8" cy="8" r="7" fill="none" stroke="#3a2d00" stroke-width="1.3"/><path d="M4.8 8.2 7 10.3l4.3-4.5" fill="none" stroke="#3a2d00" stroke-width="1.5"/></svg>Fast Delivery</li>
      <li><svg width="16" height="16" viewBox="0 0 16 16"><circle cx="8" cy="8" r="7" fill="none" stroke="#3a2d00" stroke-width="1.3"/><path d="M4.8 8.2 7 10.3l4.3-4.5" fill="none" stroke="#3a2d00" stroke-width="1.5"/></svg>The Finest Products</li>
    </ul>
  </div>
  <div class="abs pay-badge"><i></i></div>
  <div class="abs discounts"><svg width="34" height="16" viewBox="0 0 34 16"><path d="M1 3h8M4 7h6M7 11h4" stroke="#fff" stroke-width="1.3"/><rect x="14" y="1" width="19" height="14" fill="none" stroke="#fff" stroke-width="1.3"/><path d="M14 1l9.5 8L33 1" fill="none" stroke="#fff" stroke-width="1.3"/></svg>Get Discounts</div>

  <div class="abs section-title">GARDEN SUPPLIES</div>

  <div class="abs product" style="left:181px;top:43px"><span class="photo" role="img" aria-label="Close-up of green lawn turf" style="background:linear-gradient(#5fa52e,#3f8a1e)"></span><p>Turf</p></div>
  <div class="abs product" style="left:367px;top:43px"><span class="photo" role="img" aria-label="Grass shoots above a cross-section of topsoil" style="background:linear-gradient(#7dd43a 0%,#4e9a20 50%,#5a3a22 55%,#3e2716 100%)"></span><p>Topsoil</p></div>
  <div class="abs product" style="left:554px;top:43px"><span class="photo" role="img" aria-label="Hands holding rich dark compost" style="background:radial-gradient(circle at 55% 45%,#3a2a20,#6b5a50 70%,#d8cfc8)"></span><p>Compost &amp; Manures</p></div>

  <div class="abs product" style="left:183px;top:198px"><span class="photo" role="img" aria-label="Hand scooping building sand" style="background:linear-gradient(135deg,#c8a870,#b08d55)"></span><p>Sand &amp; Building Materials</p></div>
  <div class="abs product" style="left:367px;top:198px"><span class="photo" role="img" aria-label="Pile of bark chippings" style="background:linear-gradient(135deg,#8a5a40,#4a2a1c)"></span><p style="margin-top:10px">Bark</p></div>
  <div class="abs product" style="left:554px;top:198px"><span class="photo" role="img" aria-label="Pile of pale rounded gravel stones" style="background:linear-gradient(135deg,#b8b2a8,#8d867c)"></span><p style="margin-top:10px">Gravel</p></div>

  <div class="abs product" style="left:183px;top:361px"><span class="photo" role="img" aria-label="Plum coloured slate chippings" style="background:linear-gradient(135deg,#9a7a88,#5e4650)"></span><p>Slate</p></div>
  <div class="abs product" style="left:367px;top:361px"><span class="photo" role="img" aria-label="Green wheelbarrow standing on grass" style="background:linear-gradient(#7fa060,#4f6e34)"></span><p style="margin-top:10px">Wheelbarrows</p></div>
  <div class="abs product" style="left:554px;top:361px"><span class="photo" role="img" aria-label="Lettuce growing in a raised wooden bed" style="background:radial-gradient(circle at 50% 35%,#8fd04a,#4a8a20 45%,#6a3f26 70%,#4a2a18)"></span><p style="margin-top:10px">Raised Bed Kits</p></div>
</main>

<section class="abs footer-col" style="left:185px">
  <h3>QUICK LINKS</h3>
  <ul><li>Home</li><li>About Us</li><li>Garden Guru</li><li>Bulk Loads</li><li>Go To</li></ul>
</section>
<div class="abs vsep" style="left:298px"></div>
<section class="abs footer-col" style="left:333px;width:160px">
  <h3 style="font-size:10px;margin-bottom:6px">Order online before 1.00pm for next day delivery or book a delivery date!</h3>
  <ul style="line-height:22.5px"><li>Great Value</li><li>Quality Service</li><li>Fast Delivery</li><li>The Finest Products</li></ul>
</section>
<div class="abs vsep" style="left:516px"></div>
<section class="abs footer-col" style="left:551px;width:180px">
  <h3>CONTACT DETAILS</h3>
  <div style="display:flex;gap:10px;margin-bottom:8px"><svg width="10" height="14" viewBox="0 0 10 14"><path d="M5 13C1 8 1 6.5 1 5a4 4 0 0 1 8 0c0 1.5 0 3-4 8z" fill="#cfe3a9"/></svg><span>Sales Office, 14 Mill Lane<br>Brackwood Shropshire<br>SY9 4QT</span></div>
  <div style="display:flex;gap:10px;margin-bottom:9px"><svg width="10" height="11" viewBox="0 0 10 11"><path d="M1 1c1.5 5 4 7.5 8 9l1-2-2.5-1.3-1 1c-1.5-.7-2.7-2-3.4-3.4l1-1L3 0z" fill="#cfe3a9"/></svg>0870 555 2146</div>
  <div style="display:flex;gap:10px;margin-bottom:9px"><svg width="13" height="11" viewBox="0 0 13 11"><rect x="3" y="0" width="7" height="4" fill="#cfe3a9"/><rect x="0" y="4" width="13" height="7" fill="#cfe3a9"/></svg>01632 480 912</div>
  <div style="display:flex;gap:10px"><svg width="13" height="9" viewBox="0 0 13 9"><rect width="13" height="9" fill="#cfe3a9"/><path d="M0 0l6.5 5L13 0" fill="none" stroke="#5f8a26"/></svg>info@theloamfieldstore.co.uk</div>
</section>
<div class="abs vsep" style="left:737px"></div>
<div class="abs foot-brand"><i></i>The Loamfield<br>Store</div>

<div class="abs foot-rule"></div>
<p class="abs copy">©2014 <b>TheLoamfieldStore</b>. All Rights Reserved.</p>
<div class="abs social foot-social"><i style="background:#3b5998"></i><i style="background:#4aa3df"></i><i style="background:#1a79b5"></i><i style="background:#d9382c"></i></div>
</body>
</html>
```